Thornwell Building Company - advertisement poster

I am looking to print some canvas signs to advertise my general contracting company, Thornwell Building Company. The sign will measure 6' long x 3' high so the size should match that ratio. I already have a logo icon, which is the Letter 'T' and some trees that I would like to incorporate, see attached. I would also like the to have the following information listed:
1) phone number: 472-555-0188
2) email: thornwellbuildingcompany@mailvero.com
3) website: thornwellbuildingcompany.com
4) Lic#4620385
5) I want to use this text: "BUILD WITH THE T-CREW!"

The ad should be relatively simple and clean. Black and Green are my company colors. I am open to creative ideas!

Target Market(s)

People looking to renovate their homes

Industry/Entity Type

Construction

Colors
59FF00
82FF00
B8FF75
E3FFCB
F4FFEA

Requirements
Must have
• Must have my company logo
Should not have
• No photos or complex graphics

```html
<!DOCTYPE html>
<html lang="en">
<head>
<meta charset="UTF-8">
<title>Thornwell Building Company – Canvas Sign</title>
<link href="https://fonts.googleapis.com/css2?family=Bebas+Neue&family=Krona+One&family=Poppins:wght@500;700&display=swap" rel="stylesheet">
<style>
  :root {
    --backdrop: #cbcbcb;
    --ink: #1c1c1c;
    --brand-green: #6db446;
    --navy: #15206b;
    --white: #ffffff;
  }
  * { margin: 0; padding: 0; box-sizing: border-box; }
  html, body {
    width: 1200px; height: 674px; overflow: hidden;
    background: var(--backdrop);
  }
  .sign {
    position: absolute; left: 0; top: 37px;
    width: 1200px; height: 600px;
    display: flex; flex-direction: column;
  }
  .sign-top {
    height: 307px; background: var(--ink); position: relative;
  }
  .brand-name {
    position: absolute; left: 40px; top: 120px; width: 360px;
    color: var(--white);
    font-family: "Krona One", sans-serif; font-weight: 400;
    text-align: center;
  }
  .brand-name .primary { display: block; font-size: 38px; line-height: 1; letter-spacing: -1px; }
  .brand-name .secondary { display: block; font-size: 16.5px; line-height: 1; margin-top: 12px; letter-spacing: 3px; }
  .headline {
    position: absolute; left: 478px; top: 50px; width: 668px;
    text-align: left;
  }
  .headline-top {
    display: block; color: var(--brand-green);
    font-family: "Bebas Neue", sans-serif; font-size: 141px;
    line-height: 0.82; white-space: nowrap;
  }
  .headline-bottom {
    display: block; color: var(--white);
    font-family: "Krona One", sans-serif; font-size: 104px;
    line-height: 1; margin-top: 8px; letter-spacing: -3px; white-space: nowrap;
  }
  .sign-phone {
    height: 111px; background: var(--white);
    display: flex; align-items: center; position: relative;
  }
  .phone-icon { position: absolute; left: 56px; top: 12px; width: 78px; height: 78px; }
  .phone-number {
    position: absolute; left: 168px; top: 4px;
    font-family: "Krona One", sans-serif; font-size: 88px;
    color: var(--ink); line-height: 100px; letter-spacing: -1px; white-space: nowrap;
  }
  .sign-bottom {
    flex: 1; background: var(--brand-green); position: relative;
  }
  .licence {
    position: absolute; left: 46px; top: 23px; width: 209px; height: 101px;
    border: 3px solid var(--navy); border-radius: 5px; overflow: hidden;
    font-family: "Poppins", sans-serif; text-align: center; color: var(--white);
  }
  .licence-label {
    background: var(--navy); height: 46px; line-height: 48px;
    font-size: 32px; font-weight: 500;
  }
  .licence-number { line-height: 50px; font-size: 33px; font-weight: 700; }
  .contact {
    position: absolute; left: 325px; display: flex; align-items: center;
    font-family: "Poppins", sans-serif; font-weight: 500;
    color: var(--white); font-size: 32px; white-space: nowrap;
  }
  .contact-email { top: 22px; }
  .contact-web { top: 81px; }
  .contact svg { width: 40px; height: 40px; margin-right: 24px; flex: none; }
</style>
</head>
<body>
  <main class="sign">
    <section class="sign-top">
      <div class="brand-name">
        <span class="primary">THORNWELL</span>
        <span class="secondary">BUILDING COMPANY</span>
      </div>
      <h1 class="headline">
        <span class="headline-top">BUILD WITH THE</span>
        <span class="headline-bottom">T-CREW!</span>
      </h1>
    </section>

    <section class="sign-phone">
      <svg class="phone-icon" viewBox="0 0 78 78" aria-hidden="true">
        <circle cx="39" cy="39" r="39" fill="var(--navy)"/>
        <path d="M25 20c2-2 5-2 6 1l4 8c1 2 0 4-2 5l-3 2c2 6 6 10 12 13l2-3c1-2 3-3 5-2l8 4c3 1 3 4 1 6l-3 3c-3 3-9 3-15-1-8-5-14-12-18-20-3-6-3-11-1-13z" fill="var(--white)"/>
        <path d="M43 22a14 14 0 0 1 13 13" stroke="var(--white)" stroke-width="3" fill="none" stroke-linecap="round"/>
        <path d="M43 29a7 7 0 0 1 6 6" stroke="var(--white)" stroke-width="3" fill="none" stroke-linecap="round"/>
      </svg>
      <div class="phone-number">472-555-0188</div>
    </section>

    <section class="sign-bottom">
      <div class="licence">
        <div class="licence-label">Licence</div>
        <div class="licence-number">#4620385</div>
      </div>
      <div class="contact contact-email">
        <svg viewBox="0 0 40 40" aria-hidden="true">
          <circle cx="20" cy="20" r="20" fill="var(--navy)"/>
          <rect x="10" y="13" width="20" height="14" rx="1" fill="none" stroke="var(--white)" stroke-width="2"/>
          <path d="M10 14l10 8 10-8M10 26l7-6M30 26l-7-6" fill="none" stroke="var(--white)" stroke-width="2"/>
        </svg>
        thornwellbuildingcompany@mailvero.com
      </div>
      <div class="contact contact-web">
        <svg viewBox="0 0 40 40" aria-hidden="true">
          <circle cx="20" cy="20" r="20" fill="var(--navy)"/>
          <circle cx="20" cy="20" r="10" fill="none" stroke="var(--white)" stroke-width="2"/>
          <ellipse cx="20" cy="20" rx="4.5" ry="10" fill="none" stroke="var(--white)" stroke-width="2"/>
          <path d="M10 20h20M12 15h16M12 25h16" stroke="var(--white)" stroke-width="1.6"/>
        </svg>
        www.thornwellbuildingcompany.com
      </div>
    </section>
  </main>
</body>
</html>
```